Wheels and Haulers OnOffer Price Sheet

Front and back marketing / Price Sheet hand-out. 5.5 x 8.5 Attached find images you can use and basic text data. We are looking for an innovated designer that can take this data and create an appealing hand-out that will be presented to car dealerships.
The related website is www.wheelsandhaulers.onoffer
Sleek, aggressive, impressive, appealing to an age range of 30+. Professional clientele suits.
We list car ads on our VIMBA TV network and on our website. Our customers are national car / truck dealerships and individuals who want to sell a vehicle. This hand-out should advertise our company, our services and give them a look at our basic pricing.
Updates

We were so super pleased with the very first design that we boosted our budget up by 25%! You guys have talent!

Project Deadline Extended
Reason: we posted this over a USA holiday and think we can get more designs if we extend

Target Market(s)

Car and Truck Dealers across the USA

Industry/Entity Type

Marketing

Font styles to use
Serif
Sans Serif

Requirements
Must have
• Clarity in defining the price plans. The wire frame of the cars and the ON OFFER sign as seen in the provided image.

```html
<!DOCTYPE html>
<html lang="en">
<head>
<meta charset="utf-8">
<title>Wheels and Haulers OnOffer – Price Sheet</title>
<link href="https://fonts.googleapis.com/css2?family=Playfair+Display:wght@600&family=Arimo:wght@400;700&family=Russo+One&display=swap" rel="stylesheet">
<style>
  :root {
    --page-bg: #8f8f8f;
    --sheet-dark: #1b1a1a;
    --hero-dark: #262525;
    --orange: #f26522;
    --red: #d41f2b;
    --white: #ffffff;
    --silver-light: #e6e6e6;
    --silver-mid: #a9a9a9;
    --silver-dark: #6d6d6d;
    --rule: #9a9a9a;
  }
  * { box-sizing: border-box; margin: 0; padding: 0; }
  html, body { width: 1200px; height: 1200px; overflow: hidden; }
  body {
    background: var(--page-bg);
    font-family: "Arimo", Arial, sans-serif;
    color: var(--white);
  }
  .flyer {
    position: absolute;
    left: 248px; top: 52px;
    width: 706px; height: 1090px;
    background: var(--sheet-dark);
    overflow: hidden;
  }
  .top-bar { height: 12px; background: var(--orange); }
  .hero {
    position: relative;
    height: 392px;
    background: radial-gradient(ellipse at 40% 30%, #3a3939 0%, var(--hero-dark) 60%, #151414 100%);
  }
  .hero-title {
    position: absolute;
    left: 18px; top: 18px;
    font-family: "Playfair Display", Georgia, serif;
    font-weight: 600;
    color: var(--silver-light);
    line-height: 1;
    text-shadow: 0 2px 0 var(--silver-dark), 0 4px 6px rgba(0,0,0,.6);
  }
  .hero-title .line-one { display: block; font-size: 82px; }
  .hero-title .amp { font-size: 58px; }
  .hero-title .line-two { display: block; font-size: 82px; margin-left: 40px; margin-top: 6px; }
  .sale-sign {
    position: absolute;
    left: 424px; top: 17px;
    width: 210px; height: 136px;
    background: var(--red);
    padding: 8px;
    box-shadow: 0 4px 10px rgba(0,0,0,.5);
  }
  .sale-sign-inner {
    height: 100%;
    border: 4px solid var(--white);
    display: flex; flex-direction: column; justify-content: center; align-items: center;
    font-family: "Arimo", Arial, sans-serif;
    font-weight: 700;
    font-size: 40px;
    line-height: 1.02;
    color: var(--white);
  }
  .vehicle-illustration {
    position: absolute;
    left: 0; bottom: 0;
    width: 100%; height: 210px;
    background: linear-gradient(180deg, rgba(40,40,40,0) 0%, #2e2d2d 35%, #3b3a3a 70%, #232222 100%);
  }
  .hero-rule { height: 4px; background: var(--orange); }
  .intro {
    padding: 22px 48px 0;
    text-align: center;
    font-size: 18.5px;
    line-height: 1.38;
  }
  .intro .brand { color: var(--orange); font-weight: 700; }
  .price-frame {
    margin: 24px auto 0;
    width: 592px; height: 238px;
    padding: 5px;
    background: linear-gradient(135deg, var(--silver-light), var(--silver-mid) 40%, var(--silver-dark) 70%, var(--silver-light));
    clip-path: polygon(0 0, 96% 0, 100% 9%, 100% 100%, 4% 100%, 0 91%);
  }
  .price-table {
    height: 100%;
    background: linear-gradient(180deg, #333 0%, #141414 100%);
    clip-path: polygon(0 0, 96% 0, 100% 9%, 100% 100%, 4% 100%, 0 91%);
    padding: 8px 24px;
    text-align: center;
  }
  .plan { padding: 5px 0 6px; border-bottom: 1px solid var(--rule); }
  .plan:last-child { border-bottom: none; }
  .plan-name { color: var(--orange); font-weight: 700; font-size: 20px; line-height: 1.2; }
  .plan-terms { font-size: 18px; line-height: 1.3; }
  .notes {
    padding: 18px 60px 0;
    text-align: center;
    font-size: 19px;
    line-height: 1.32;
  }
  .contact { text-align: center; margin-top: 20px; }
  .phone { font-family: "Russo One", Arial, sans-serif; font-size: 35px; letter-spacing: 1px; }
  .website { color: var(--orange); font-weight: 700; font-size: 21px; margin-top: 2px; }
  .checker-band {
    position: absolute;
    left: 0; bottom: 6px;
    width: 100%; height: 38px;
    background: linear-gradient(180deg, #d8d8d8, #9c9c9c);
  }
</style>
</head>
<body>
  <main class="flyer">
    <div class="top-bar"></div>
    <header class="hero">
      <h1 class="hero-title">
        <span class="line-one">Wheels <span class="amp">&amp;</span></span>
        <span class="line-two">Haulers</span>
      </h1>
      <div class="sale-sign"><div class="sale-sign-inner"><span>ON</span><span>OFFER</span></div></div>
      <div class="vehicle-illustration" role="img" aria-label="Wireframe drawings of a pickup truck and a sports car"></div>
    </header>
    <div class="hero-rule"></div>

    <p class="intro">
      <span class="brand">WHEELS AND HAULERS ON OFFER</span> is a unique opportunity that allows you to further your reach with an ad on our VIMBA TV channel and also on our website. VIMBA offers the biggest streaming line-up with 2000+ channels and more than 10 million VIMBA devices sold; so your potential buyers just exploded! Wheels and Haulers On Offer can be found in the VIMBA channel store in the Shopping Category.
    </p>

    <div class="price-frame">
      <div class="price-table">
        <div class="plan">
          <div class="plan-name">Special Deal</div>
          <div class="plan-terms">$1 a day / 1 ad for 30 days minumum.</div>
        </div>
        <div class="plan">
          <div class="plan-name">Dealer Package</div>
          <div class="plan-terms">90¢ a day / 10 ads for 90 days minumum.</div>
        </div>
        <div class="plan">
          <div class="plan-name">Bonus Dealer Package</div>
          <div class="plan-terms">90¢ a day / 10 ads for 90 days minmum PLUS 3<br>featured vehicles on both VIMBA TV and the WEB</div>
        </div>
      </div>
    </div>

    <p class="notes">Featured packages may be bought as add-ons. If you want a larger package please call us we offer an execute package for the elite client.</p>

    <div class="contact">
      <div class="phone">555-013-4820</div>
      <div class="website">wheelsandhaulers.onoffer</div>
    </div>

    <div class="checker-band" role="img" aria-label="Checkered flag band"></div>
  </main>
</body>
</html>
```